" Fazer o calendário de parede conforme o anexo abaixo sendo que a parte para fazer o cabeçalho tem que ter a medida 41cm de comprimento por 11,5cm de altura "

```html
<!DOCTYPE html>
<html lang="pt-BR">
<head>
<meta charset="UTF-8">
<title>Calendário 2026 – Verdejar Hortifruti</title>
<link href="https://fonts.googleapis.com/css2?family=Montserrat:wght@400;500;600;700;800&display=swap" rel="stylesheet">
<style>
  :root {
    --backdrop: #e9a58c;
    --paper: #ffffff;
    --green-dark: #1d5a24;
    --green: #2f7d34;
    --green-light: #4f9c45;
    --crimson: #d8234f;
    --ink: #3a3a3a;
    --muted: #8a8a8a;
    --weekend: #e2473f;
    --weekend-bg: #fdecea;
  }
  * { box-sizing: border-box; margin: 0; padding: 0; }
  html, body { width: 1200px; height: 1200px; overflow: hidden; }
  body {
    background: var(--backdrop);
    font-family: "Montserrat", sans-serif;
    display: flex; align-items: center; justify-content: center;
  }
  .calendar-sheet {
    width: 780px; height: 1150px;
    background: var(--paper);
    display: flex; flex-direction: column;
  }
  .calendar-header {
    height: 219px;
    position: relative;
    background: linear-gradient(100deg, var(--green-dark), var(--green) 45%, var(--green-light));
    display: flex; align-items: center;
    padding-left: 38px;
  }
  .brand {
    display: flex; align-items: center; gap: 16px;
    color: #ffffff; font-weight: 800;
  }
  .brand-dot { width: 44px; height: 44px; border-radius: 50%; background: #ffffff; }
  .brand-name { font-size: 44px; line-height: 1; }
  .brand-name small { display: block; font-size: 20px; letter-spacing: 4px; margin-top: 6px; }
  .fruit-photo {
    position: absolute; right: 0; top: 70px; bottom: 0; width: 330px;
    background: radial-gradient(circle at 30% 60%, #e53935 0 22%, transparent 23%),
                radial-gradient(circle at 78% 55%, #e8454a 0 30%, #3f8f3a 31% 36%, transparent 37%),
                linear-gradient(120deg, #2f7d34, #4f9c45);
  }
  .year-box {
    position: absolute; right: 120px; top: 0;
    width: 180px; height: 130px;
    background: var(--crimson); color: #fff;
    display: flex; flex-direction: column; align-items: center; justify-content: center;
  }
  .year-box .year { font-size: 56px; font-weight: 700; line-height: 1; }
  .year-box .label { font-size: 15px; font-weight: 500; letter-spacing: 2px; margin-top: 6px; }

  .months {
    flex: 1;
    display: grid;
    grid-template-columns: repeat(3, 1fr);
    grid-template-rows: repeat(4, 1fr);
    padding: 26px 34px 30px;
    column-gap: 30px;
  }
  .month h2 {
    text-align: center; font-size: 21px; font-weight: 600;
    color: var(--ink); margin-bottom: 10px;
  }
  .weekdays, .days {
    display: grid; grid-template-columns: repeat(7, 1fr); text-align: center;
  }
  .weekdays span { font-size: 8px; color: var(--muted); font-weight: 600; padding: 3px 0; }
  .weekdays span:nth-child(n+6) { color: var(--weekend); background: var(--weekend-bg); }
  .days span { font-size: 14px; font-weight: 500; color: var(--ink); line-height: 23px; }
  .days span:nth-child(7n+6), .days span:nth-child(7n) { color: var(--weekend); background: var(--weekend-bg); }
</style>
</head>
<body>
<main class="calendar-sheet">
  <header class="calendar-header">
    <div class="brand"><span class="brand-dot"></span><span class="brand-name">Verdejar<small>HORTIFRUTI</small></span></div>
    <div class="fruit-photo" role="img" aria-label="Foto de morangos e fatia de melancia"></div>
    <div class="year-box"><span class="year">2026</span><span class="label">CALENDÁRIO</span></div>
  </header>

  <section class="months">
    <div class="month"><h2>Janeiro</h2><div class="weekdays"><span>SEG</span><span>TER</span><span>QUA</span><span>QUI</span><span>SEX</span><span>SAB</span><span>DOM</span></div>
      <div class="days"><span></span><span></span><span></span><span>1</span><span>2</span><span>3</span><span>4</span><span>5</span><span>6</span><span>7</span><span>8</span><span>9</span><span>10</span><span>11</span><span>12</span><span>13</span><span>14</span><span>15</span><span>16</span><span>17</span><span>18</span><span>19</span><span>20</span><span>21</span><span>22</span><span>23</span><span>24</span><span>25</span><span>26</span><span>27</span><span>28</span><span>29</span><span>30</span><span>31</span></div></div>
    <div class="month"><h2>Fevereiro</h2><div class="weekdays"><span>SEG</span><span>TER</span><span>QUA</span><span>QUI</span><span>SEX</span><span>SAB</span><span>DOM</span></div>
      <div class="days"><span></span><span></span><span></span><span></span><span></span><span></span><span>1</span><span>2</span><span>3</span><span>4</span><span>5</span><span>6</span><span>7</span><span>8</span><span>9</span><span>10</span><span>11</span><span>12</span><span>13</span><span>14</span><span>15</span><span>16</span><span>17</span><span>18</span><span>19</span><span>20</span><span>21</span><span>22</span><span>23</span><span>24</span><span>25</span><span>26</span><span>27</span><span>28</span></div></div>
    <div class="month"><h2>Março</h2><div class="weekdays"><span>SEG</span><span>TER</span><span>QUA</span><span>QUI</span><span>SEX</span><span>SAB</span><span>DOM</span></div>
      <div class="days"><span></span><span></span><span></span><span></span><span></span><span></span><span>1</span><span>2</span><span>3</span><span>4</span><span>5</span><span>6</span><span>7</span><span>8</span><span>9</span><span>10</span><span>11</span><span>12</span><span>13</span><span>14</span><span>15</span><span>16</span><span>17</span><span>18</span><span>19</span><span>20</span><span>21</span><span>22</span><span>23</span><span>24</span><span>25</span><span>26</span><span>27</span><span>28</span><span>29</span><span>30</span><span>31</span></div></div>
    <div class="month"><h2>Abril</h2><div class="weekdays"><span>SEG</span><span>TER</span><span>QUA</span><span>QUI</span><span>SEX</span><span>SAB</span><span>DOM</span></div>
      <div class="days"><span></span><span></span><span>1</span><span>2</span><span>3</span><span>4</span><span>5</span><span>6</span><span>7</span><span>8</span><span>9</span><span>10</span><span>11</span><span>12</span><span>13</span><span>14</span><span>15</span><span>16</span><span>17</span><span>18</span><span>19</span><span>20</span><span>21</span><span>22</span><span>23</span><span>24</span><span>25</span><span>26</span><span>27</span><span>28</span><span>29</span><span>30</span></div></div>
    <div class="month"><h2>Maio</h2><div class="weekdays"><span>SEG</span><span>TER</span><span>QUA</span><span>QUI</span><span>SEX</span><span>SAB</span><span>DOM</span></div>
      <div class="days"><span></span><span></span><span></span><span></span><span>1</span><span>2</span><span>3</span><span>4</span><span>5</span><span>6</span><span>7</span><span>8</span><span>9</span><span>10</span><span>11</span><span>12</span><span>13</span><span>14</span><span>15</span><span>16</span><span>17</span><span>18</span><span>19</span><span>20</span><span>21</span><span>22</span><span>23</span><span>24</span><span>25</span><span>26</span><span>27</span><span>28</span><span>29</span><span>30</span><span>31</span></div></div>
    <div class="month"><h2>Junho</h2><div class="weekdays"><span>SEG</span><span>TER</span><span>QUA</span><span>QUI</span><span>SEX</span><span>SAB</span><span>DOM</span></div>
      <div class="days"><span>1</span><span>2</span><span>3</span><span>4</span><span>5</span><span>6</span><span>7</span><span>8</span><span>9</span><span>10</span><span>11</span><span>12</span><span>13</span><span>14</span><span>15</span><span>16</span><span>17</span><span>18</span><span>19</span><span>20</span><span>21</span><span>22</span><span>23</span><span>24</span><span>25</span><span>26</span><span>27</span><span>28</span><span>29</span><span>30</span></div></div>
    <div class="month"><h2>Julho</h2><div class="weekdays"><span>SEG</span><span>TER</span><span>QUA</span><span>QUI</span><span>SEX</span><span>SAB</span><span>DOM</span></div>
      <div class="days"><span></span><span></span><span>1</span><span>2</span><span>3</span><span>4</span><span>5</span><span>6</span><span>7</span><span>8</span><span>9</span><span>10</span><span>11</span><span>12</span><span>13</span><span>14</span><span>15</span><span>16</span><span>17</span><span>18</span><span>19</span><span>20</span><span>21</span><span>22</span><span>23</span><span>24</span><span>25</span><span>26</span><span>27</span><span>28</span><span>29</span><span>30</span><span>31</span></div></div>
    <div class="month"><h2>Agosto</h2><div class="weekdays"><span>SEG</span><span>TER</span><span>QUA</span><span>QUI</span><span>SEX</span><span>SAB</span><span>DOM</span></div>
      <div class="days"><span></span><span></span><span></span><span></span><span></span><span>1</span><span>2</span><span>3</span><span>4</span><span>5</span><span>6</span><span>7</span><span>8</span><span>9</span><span>10</span><span>11</span><span>12</span><span>13</span><span>14</span><span>15</span><span>16</span><span>17</span><span>18</span><span>19</span><span>20</span><span>21</span><span>22</span><span>23</span><span>24</span><span>25</span><span>26</span><span>27</span><span>28</span><span>29</span><span>30</span><span>31</span></div></div>
    <div class="month"><h2>Setembro</h2><div class="weekdays"><span>SEG</span><span>TER</span><span>QUA</span><span>QUI</span><span>SEX</span><span>SAB</span><span>DOM</span></div>
      <div class="days"><span></span><span>1</span><span>2</span><span>3</span><span>4</span><span>5</span><span>6</span><span>7</span><span>8</span><span>9</span><span>10</span><span>11</span><span>12</span><span>13</span><span>14</span><span>15</span><span>16</span><span>17</span><span>18</span><span>19</span><span>20</span><span>21</span><span>22</span><span>23</span><span>24</span><span>25</span><span>26</span><span>27</span><span>28</span><span>29</span><span>30</span></div></div>
    <div class="month"><h2>Outubro</h2><div class="weekdays"><span>SEG</span><span>TER</span><span>QUA</span><span>QUI</span><span>SEX</span><span>SAB</span><span>DOM</span></div>
      <div class="days"><span></span><span></span><span></span><span>1</span><span>2</span><span>3</span><span>4</span><span>5</span><span>6</span><span>7</span><span>8</span><span>9</span><span>10</span><span>11</span><span>12</span><span>13</span><span>14</span><span>15</span><span>16</span><span>17</span><span>18</span><span>19</span><span>20</span><span>21</span><span>22</span><span>23</span><span>24</span><span>25</span><span>26</span><span>27</span><span>28</span><span>29</span><span>30</span><span>31</span></div></div>
    <div class="month"><h2>Novembro</h2><div class="weekdays"><span>SEG</span><span>TER</span><span>QUA</span><span>QUI</span><span>SEX</span><span>SAB</span><span>DOM</span></div>
      <div class="days"><span></span><span></span><span></span><span></span><span></span><span></span><span>1</span><span>2</span><span>3</span><span>4</span><span>5</span><span>6</span><span>7</span><span>8</span><span>9</span><span>10</span><span>11</span><span>12</span><span>13</span><span>14</span><span>15</span><span>16</span><span>17</span><span>18</span><span>19</span><span>20</span><span>21</span><span>22</span><span>23</span><span>24</span><span>25</span><span>26</span><span>27</span><span>28</span><span>29</span><span>30</span></div></div>
    <div class="month"><h2>Dezembro</h2><div class="weekdays"><span>SEG</span><span>TER</span><span>QUA</span><span>QUI</span><span>SEX</span><span>SAB</span><span>DOM</span></div>
      <div class="days"><span></span><span>1</span><span>2</span><span>3</span><span>4</span><span>5</span><span>6</span><span>7</span><span>8</span><span>9</span><span>10</span><span>11</span><span>12</span><span>13</span><span>14</span><span>15</span><span>16</span><span>17</span><span>18</span><span>19</span><span>20</span><span>21</span><span>22</span><span>23</span><span>24</span><span>25</span><span>26</span><span>27</span><span>28</span><span>29</span><span>30</span><span>31</span></div></div>
  </section>
</main>
</body>
</html>
```